Lumen Accountants needs a stationery design

We need a stationery design for our new innovative accountancy practise - it is to look professional and reliable but also minimalist, crisp, innovative and fresh. Avoid the use of block colour. You must include letterhead.

We look after business clients and help them get started and grow to successful companies. We provide a range of software, accounting, taxation and business consulting services to these clients.

This is a spin off from our more traditional existing practise - we would like to use the same green and blue.

The final design should communicate professional expertise coupled with innovative technology and personal care. The font of the type should reflect this - so far we have received standard font only.

We need business cards, letterhead, with comp slips, We need to see the whole set to form a view, not just the businesscard

I have uploaded the colours that we want to use from our existing letterhead, being the green and blue. We need to use the RFQ logo - also enclosed - please use the text from the enclosed letterhead, but don't refer to this for design purposes - this was our temporary draft only.

Target Market(s)

Small to medium companies, high wealth investor clients

Industry/Entity Type

Professional Service

Requirements
Must have
• Crisp, simple design but evoking innovation, technology, competence and difference.
• So far the designs are too standard and not showing innovation.

```html
<!DOCTYPE html>
<html lang="en">
<head>
<meta charset="utf-8">
<title>Lumen Accountants — Stationery Set</title>
<link href="https://fonts.googleapis.com/css2?family=Jost:wght@400;500&family=Open+Sans:wght@400;600&family=PT+Sans&display=swap" rel="stylesheet">
<style>
:root{
  --backdrop:#a9a9a9;
  --paper:#f5f4f1;
  --green:#7a9a2e;
  --blue:#3a6096;
  --navy:#1f3f6e;
  --ink:#3c3c3c;
  --card-blue:#365b8c;
  --rule:#8a8a8a;
}
*{margin:0;padding:0;box-sizing:border-box}
html,body{width:1200px;height:622px;overflow:hidden;background:var(--backdrop)}
body{position:relative;font-family:"Jost",sans-serif;color:var(--ink)}
.sheet{position:absolute;background:var(--paper);box-shadow:0 2px 6px rgba(0,0,0,.25);overflow:hidden}
.edge-bar{position:absolute;left:0;top:0;bottom:0;width:5px;background:var(--blue)}
.edge-bar::before{content:"";position:absolute;left:0;top:0;width:100%;height:var(--green-h,34px);background:var(--green)}
.brand{position:absolute;font-family:"Open Sans",sans-serif;color:var(--blue);font-weight:400;white-space:nowrap;line-height:1}
.icon{width:6px;height:6px;vertical-align:-1px;fill:var(--navy)}

/* Letterhead */
.letterhead{left:281px;top:26px;width:400px;height:566px}
.letterhead .edge-bar{--green-h:92px}
.letterhead .brand{left:30px;top:60px;font-size:13px}
.letterhead .address{position:absolute;right:30px;top:42px;text-align:right;font-size:6px;line-height:7.6px;color:var(--ink)}
.letterhead .address strong{color:var(--navy);font-weight:500;display:block;margin-bottom:4px}
.letterhead .address p+p{margin-top:3px}
.salutation{position:absolute;left:30px;top:160px;font-family:"PT Sans",sans-serif;font-size:10.5px}
.letter-body{position:absolute;left:30px;top:190px;width:343px;font-family:"PT Sans",sans-serif;font-size:5.8px;line-height:10px;text-align:justify}
.letter-body p+p{margin-top:10px}
.sign-off{position:absolute;left:30px;top:394px;font-family:"PT Sans",sans-serif;font-size:5.8px}
.signature{position:absolute;left:39px;top:410px;width:52px;height:20px;background:linear-gradient(90deg,#d9d8d4,#c9c8c4)}
.signatory{position:absolute;left:42px;top:438px;font-family:"PT Sans",sans-serif;font-size:6px;line-height:10px}
.letter-footer{position:absolute;left:0;right:0;top:540px;text-align:center;font-size:6px}
.letter-footer span{margin:0 2px}

/* Compliments slip */
.comp-slip{left:705px;top:157px;width:453px;height:205px}
.comp-slip .brand{left:26px;top:36px;font-size:13.5px}
.comp-title{position:absolute;right:31px;top:38px;font-family:"Jost",sans-serif;font-size:18px;color:var(--navy)}
.slip-footer{position:absolute;left:23px;right:31px;top:166px;text-align:center;font-size:6.4px;color:var(--navy)}
.slip-footer hr{border:0;border-top:.7px solid var(--rule);margin:4px 0 3px}

/* Address slip */
.address-slip{left:705px;top:387px;width:453px;height:205px}
.address-slip .brand{left:26px;top:22px;font-size:14.5px}
.address-slip .details{position:absolute;left:26px;top:58px;font-size:6.2px;line-height:7.6px;color:var(--navy)}
.address-slip .details p+p{margin-top:3px}

/* Business card */
.card-front{left:85px;top:196px;width:123px;height:216px}
.card-front .brand{left:0;right:0;top:20px;text-align:center;font-size:9.8px}
.card-front .edge-bar{top:110px;bottom:16px;width:4px;--green-h:16px}
.card-front .holder{position:absolute;left:11px;top:109px;font-size:8.6px;font-weight:500;color:var(--navy)}
.card-front .role{position:absolute;left:11px;top:119px;font-size:5px;color:var(--green)}
.card-front .details{position:absolute;left:11px;top:128px;font-size:4.6px;line-height:5.6px;color:var(--navy)}
.card-front .details p+p{margin-top:2px}
.card-front .contact{margin-top:4px}
.card-front .contact div{line-height:7.4px}
.card-back{left:38px;top:442px;width:216px;height:123px;background:var(--card-blue)}
.member-mark{position:absolute;left:176px;top:14px;width:29px;height:13px;background:#f2d233}
.card-back .brand{left:0;right:0;top:52px;text-align:center;font-size:14px;color:#fff}
.card-back .legal{position:absolute;left:0;right:0;top:97px;text-align:center;font-size:5px;line-height:8px;color:#e6ecf4}
.card-back .legal strong{font-weight:500;color:#fff;font-size:5.4px}
</style>
</head>
<body>

<svg width="0" height="0" style="position:absolute" aria-hidden="true">
  <symbol id="i-phone" viewBox="0 0 10 10"><path d="M2.2 1l1.6 2-1 1.1c.6 1.3 1.7 2.4 3 3l1.1-1 2 1.6-.9 1.6C4.6 9.3.7 5.4.6 1.9z"/></symbol>
  <symbol id="i-mobile" viewBox="0 0 10 10"><rect x="2.5" y="0.5" width="5" height="9" rx="1"/></symbol>
  <symbol id="i-mail" viewBox="0 0 10 10"><rect x="0.5" y="2" width="9" height="6"/><path d="M0.5 2l4.5 3.5L9.5 2" stroke="#fff" stroke-width=".8" fill="none"/></symbol>
  <symbol id="i-web" viewBox="0 0 10 10"><circle cx="5" cy="5" r="4.5"/><path d="M.5 5h9M5 .5c-2.4 2.8-2.4 6.2 0 9M5 .5c2.4 2.8 2.4 6.2 0 9" stroke="#fff" stroke-width=".7" fill="none"/></symbol>
</svg>

<!-- Business card, front -->
<section class="sheet card-front">
  <div class="brand">Lumen Accountants</div>
  <div class="edge-bar"></div>
  <div class="holder">James Hollis</div>
  <div class="role">Accountants</div>
  <div class="details">
    <p>Lumen Accountants<br>ABN 48 302 771 915</p>
    <p>P O Box 2208, Glenwood NSW 2590<br>Suite 4B, Level 3, 12 Harbour Lane<br>Glenwood NSW 2590</p>
    <div class="contact">
      <div><svg class="icon"><use href="#i-phone"/></svg> (02) 5550 1842</div>
      <div><svg class="icon"><use href="#i-mobile"/></svg> 0400 555 917</div>
      <div><svg class="icon"><use href="#i-mail"/></svg> clients@lumenaccountants.example</div>
      <div><svg class="icon"><use href="#i-web"/></svg> www.lumenaccountants.example</div>
    </div>
  </div>
</section>

<!-- Business card, back -->
<section class="sheet card-back">
  <div class="member-mark" role="img" aria-label="Professional membership badge"></div>
  <div class="brand">Lumen Accountants</div>
  <div class="legal">Liability limited by a Scheme approved under Professional Standards Legislation<br><strong>Lumen Accountants is a RFQ Practise</strong></div>
</section>

<!-- Letterhead -->
<section class="sheet letterhead">
  <div class="edge-bar"></div>
  <div class="brand">Lumen Accountants</div>
  <div class="address">
    <strong>Lumen Accountants</strong>
    <p>Suite 4B, Level 3<br>12 Harbour Lane<br>Glenwood NSW 2590</p>
    <p>P O Box 2208<br>Glenwood NSW 2590<br>ABN 48 302 771 915</p>
  </div>
  <div class="salutation">Dear Mr. Hollis,</div>
  <div class="letter-body">
    <p>Lorem ipsum dolor sit amet, consectetur adipiscing elit. Donec orci purus, luctus vitae dignissim eu, iaculis sed purus. Vivamus faucibus, ipsum nec aliquet viverra, leo mauris condimentum ligula, sit amet sagittis enim ligula quis arcu. Nam egestas tortor id nisi porttitor mattis. In tortor ante, ultricies in suscipit a, tempus non massa. Vivamus et auctor mi. Fusce vel massa nulla. Phasellus nec eros mauris, et scelerisque orci.</p>
    <p>Donec malesuada orci vitae nulla accumsan porta a id massa. Quisque accumsan iaculis magna sit amet fringilla. Maecenas consequat, magna eget tincidunt semper, odio nibh rutrum mi, id feugiat ante nisi eu risus. Vestibulum nunc orci, rhoncus a placerat in, ultricies in mi. Cras mattis varius eros, vel fringilla nisi suscipit eget. Quisque scelerisque sagittis nulla at porttitor.</p>
    <p>Sed id augue vitae urna euismod commodo aliquet a quam. Pellentesque arcu velit, cursus et malesuada ut, consequat et diam. Nullam erat sem, rhoncus id ullamcorper vitae, rhoncus et arcu. In ultricies ultricies nulla, ut rutrum nisi iaculis at. Donec eu magna a metus ornare faucibus. Fusce aliquet faucibus ultricies. Morbi semper, est id tincidunt gravida, sem arcu adipiscing lacus, ac bibendum nulla leo eu purus. Quisque nec diam sed risus consectetur a ccumsan quis quis nibh. Vestibulum id purus lorem.</p>
    <p>It is a long established fact that a reader will be distracted by the readable content of a page when looking at its layout. The point of using Lorem Ipsum is that it has a more-or-less normal distribution of letters, as opposed to using 'Content here, content here', making it look like readable English. Many desktop publishing packages</p>
  </div>
  <div class="sign-off">Sincerely,</div>
  <div class="signature" role="img" aria-label="Handwritten signature of the sender"></div>
  <div class="signatory">James Hollis<br>CEO/ Founder</div>
  <div class="letter-footer">
    <span><svg class="icon"><use href="#i-phone"/></svg> (02) 5550 1842</span>
    <span><svg class="icon"><use href="#i-mail"/></svg> clients@lumenaccountants.example</span>
    <span><svg class="icon"><use href="#i-web"/></svg> lumenaccountants.example</span>
  </div>
</section>

<!-- Compliments slip -->
<section class="sheet comp-slip">
  <div class="edge-bar"></div>
  <div class="brand">Lumen Accountants</div>
  <div class="comp-title">With Compliments</div>
  <div class="slip-footer">
    <div>Lumen Accountants, P O Box 2208, Glenwood NSW 2590 | Suite 4B, Level 3, 12 Harbour Lane, Glenwood NSW 2590</div>
    <hr>
    <div>(02) 5550 1842 | clients@lumenaccountants.example | www.lumenaccountants.example | ABN 48 302 771 915</div>
  </div>
</section>

<!-- Address slip -->
<section class="sheet address-slip">
  <div class="edge-bar"></div>
  <div class="brand">Lumen Accountants</div>
  <div class="details">
    <p>Lumen Accountants<br>ABN 48 302 771 915</p>
    <p>P O Box 2208, Glenwood NSW 2590</p>
    <p>Suite 4B, Level 3, 12 Harbour Lane<br>Glenwood NSW 2590</p>
  </div>
</section>

</body>
</html>
```